UK Glass Restoration Company needs a Direct Mail Postcard Design

We need a HARD HITTING, COMPELLING 300dpi Camera Ready double sided postcard.
The dimensions will be 109mm x 152mm including bleed. We are a scratched glass repair / etched graffiti removal glass restoration company based in London, UK.
We operate mainly within the construction and commercial marketplace, however this particular postcard design is aimed solely at shop owners who have become victims of vandalism, due to etched graffiti tags and or scratches being left on their shop front glass.
We wish to focus the shop / business owners mind to the negative impact such vandalism has on the image of their business and how we are able to offer a quick and cost effective solution
We will supply text for both sides of the postcard along with relevant images, company logo and previous flyer designs, however we are happy for the selected designer to source suitable alternative images provided they are in keeping with the exact "Before" and "After" theme.
The finished postcard must preferably have a white background, but again we are open to creative suggestions.
Target Market(s)
UK SHOP OWNERS
Industry/Entity Type
It Company

```html
<!DOCTYPE html>
<html lang="en">
<head>
<meta charset="utf-8">
<title>Lucent Glass Repairs – Shop Window Postcard</title>
<link rel="stylesheet" href="https://fonts.googleapis.com/css2?family=Cabin+Sketch:wght@700&family=Source+Sans+3:ital,wght@0,400;0,700;1,400&family=Roboto:ital,wght@1,700;1,900&display=swap">
<style>
  :root {
    --red: #ea2530;
    --charcoal: #383838;
    --white: #ffffff;
    --light-grey: #efefef;
    --ink: #1d1d1d;
    --muted: #555555;
    --brand-blue: #1a9ad6;
    --photo-dark: #5a3a14;
    --photo-warm: #b7832f;
  }
  * { box-sizing: border-box; margin: 0; padding: 0; }
  html, body { width: 960px; height: 1200px; overflow: hidden; }
  body {
    background: var(--white);
    font-family: "Source Sans 3", sans-serif;
    color: var(--ink);
    position: relative;
  }
  .top-band {
    position: absolute; left: 19px; right: 20px; top: 3px; height: 39px;
    background: var(--red);
  }
  .headline-panel {
    position: absolute; left: 19px; right: 20px; top: 49px; height: 226px;
    background: var(--charcoal);
    text-align: center;
  }
  .headline {
    margin-top: 20px;
    font-family: "Source Sans 3", sans-serif;
    font-weight: 700;
    font-size: 66px;
    line-height: 1;
    color: var(--red);
    letter-spacing: 1px;
  }
  .headline .scratched {
    font-family: "Cabin Sketch", cursive;
    color: var(--white);
    font-size: 70px;
  }
  .tagline {
    margin-top: 14px;
    font-family: "Roboto", sans-serif;
    font-style: italic;
    font-weight: 900;
    font-size: 50px;
    line-height: 58px;
    color: #ececec;
  }
  .photo-band {
    position: absolute; left: 19px; right: 20px; top: 285px; height: 416px;
    background: var(--light-grey);
  }
  .photo {
    position: absolute; left: 152px; top: 0; width: 617px; height: 416px;
    background: radial-gradient(ellipse at 55% 45%, var(--photo-warm), var(--photo-dark));
    border: 1px solid #222;
  }
  .caption {
    position: absolute; left: 19px; right: 20px; top: 701px; height: 32px;
    background: var(--red);
    color: var(--white);
    font-style: italic;
    font-size: 25px;
    line-height: 32px;
    text-align: center;
    letter-spacing: 0.5px;
  }
  .intro {
    position: absolute; left: 49px; right: 40px; top: 745px;
  }
  .intro-heading {
    font-style: italic;
    font-size: 31px;
    line-height: 38px;
  }
  .intro-body {
    margin-left: 3px;
    font-size: 24.5px;
    line-height: 34.5px;
  }
  .coupon-note {
    position: absolute; left: 0; right: 0; top: 960px;
    text-align: center;
    color: var(--red);
    font-size: 26px;
  }
  .call-line {
    position: absolute; left: 0; right: 0; top: 998px;
    text-align: center;
    font-size: 26px;
  }
  .call-line .phone {
    color: var(--red);
    font-weight: 700;
    font-size: 33px;
  }
  .divider {
    position: absolute; left: 80px; right: 80px; top: 1048px; height: 2px;
    background: linear-gradient(90deg, transparent, #dddddd 20%, #dddddd 80%, transparent);
  }
  .brand {
    position: absolute; left: 50px; top: 1082px;
    display: flex; align-items: center; gap: 10px;
    color: var(--brand-blue);
    font-size: 48px;
    font-weight: 400;
    line-height: 1;
  }
  .brand-dot {
    width: 18px; height: 18px; border-radius: 50%;
    background: var(--brand-blue);
  }
  .brand-sub {
    position: absolute; left: 78px; top: 1134px;
    color: var(--brand-blue);
    font-size: 18px;
    letter-spacing: 5px;
  }
  .contact {
    position: absolute; right: 48px; top: 1108px;
    text-align: right;
    font-size: 22px;
    line-height: 28px;
  }
  .contact-row { display: flex; align-items: center; justify-content: flex-end; gap: 6px; }
  .contact-row.phone-row { color: var(--muted); }
  .contact svg { width: 16px; height: 16px; }
</style>
</head>
<body>
  <div class="top-band"></div>

  <header class="headline-panel">
    <h1 class="headline">Got <span class="scratched">Scratched</span> Glass?</h1>
    <p class="tagline">Don't let vandals wreck<br>your image!</p>
  </header>

  <section class="photo-band">
    <div class="photo" role="img" aria-label="Shop window with scratched glass in front of property listing displays, before repair"></div>
  </section>
  <p class="caption">Before repair – a bad first impression.</p>

  <section class="intro">
    <h2 class="intro-heading">What's on display in your shop window?</h2>
    <p class="intro-body">If it's graffiti, vandalism, or just wear and tear, that's the first impression your customers get – and it's not good. Lucent Glass Repairs remove damage from glass windows, making them sparkling clear – without replacing the glass! Our glass repair work is effective, green, and very economical.</p>
  </section>

  <p class="coupon-note">See our coupon on the other side to save even more!</p>
  <p class="call-line">Call now for expert advice : <span class="phone">0800 555 0147</span></p>

  <div class="divider"></div>

  <div class="brand"><span>Lucent</span><span class="brand-dot"></span></div>
  <div class="brand-sub">glass repairs</div>

  <address class="contact" style="font-style:normal">
    <div class="contact-row">
      <svg viewBox="0 0 16 16" aria-hidden="true"><g fill="none" stroke="#1d1d1d" stroke-width="1.2"><circle cx="8" cy="8" r="6.5"/><ellipse cx="8" cy="8" rx="3" ry="6.5"/><line x1="1.5" y1="8" x2="14.5" y2="8"/><line x1="2.5" y1="4.5" x2="13.5" y2="4.5"/><line x1="2.5" y1="11.5" x2="13.5" y2="11.5"/></g></svg>
      <span>www.lucentglassrepairs.co.uk</span>
    </div>
    <div class="contact-row phone-row">
      <svg viewBox="0 0 16 16" aria-hidden="true"><path fill="#555" d="M3.6 1.5l2.2 2.6-1.2 1.6c.9 2 2.4 3.5 4.4 4.5l1.6-1.2 2.6 2.2-1.3 2.3C7 13 3 9 1.4 2.8z"/></svg>
      <span>0800 555 0147</span>
    </div>
  </address>
</body>
</html>
```